Custom Truck shop New Business Card design

double sided business card including my new logo, brand colors and picking a font I attached, clean and modern look. I attached the old card for some reference. and would like to include the picture of the white truck attached. I would also like to have it with one of my employees info as well. (same info except name and title Brenna Dulwick Service Writer)

Todd Varnell
Owner

address
20418 E Pinecrest Service Rd S
STE 310
Cedar Bluff, UT 80517

phone 720-384-9172

email todd@ironcanyonrigs.com

website ironcanyonrogs.com

social @ironcanyonrigs

Target Market(s)

men 18-60

Industry/Entity Type

Automotive

Contact Information for Business Card

Todd Varnell Owner address 20418 E Pinecrest Service Rd S STE 310 Cedar Bluff, UT 80517 phone 720-384-9172 email todd@ironcanyonrigs.com website ironcanyonrogs.com social @ironcanyonrigs

Font styles to use
Other font styles liked:
• fonts attached

Requirements
Must have
• new logo, orange #FC68D, Charcoal #333333
Nice to have
• the white truck

```html
<!DOCTYPE html>
<html lang="en">
<head>
<meta charset="utf-8">
<title>Iron Canyon Rigs – Business Card</title>
<link rel="stylesheet" href="https://fonts.googleapis.com/css2?family=Archivo:ital,wght@1,900&family=Figtree:wght@500;600;700&display=swap">
<style>
  :root {
    --orange: #fc6a2f;
    --charcoal: #333333;
    --white: #ffffff;
    --backdrop: #000000;
  }
  * { margin: 0; padding: 0; box-sizing: border-box; }
  html, body { width: 1200px; height: 1200px; overflow: hidden; background: var(--backdrop); }
  body { position: relative; font-family: "Figtree", sans-serif; }

  .card {
    position: absolute;
    left: 149px;
    width: 902px;
    height: 515px;
    border-radius: 68px;
    overflow: hidden;
  }
  .card--front { top: 69px; background: var(--white); }
  .card--back { top: 615px; background: var(--orange); }

  /* Front: brand block */
  .brand {
    position: absolute;
    left: 75px;
    top: 150px;
    width: 360px;
    text-align: center;
  }
  .brand__dot {
    width: 102px; height: 102px;
    margin: 0 auto 18px;
    border-radius: 50%;
    background: var(--charcoal);
  }
  .brand__name {
    font-family: "Figtree", sans-serif;
    font-weight: 700;
    font-size: 32px;
    letter-spacing: 2px;
    color: var(--charcoal);
    white-space: nowrap;
  }

  /* Front: person + contacts */
  .person {
    position: absolute;
    left: 543px;
    top: 143px;
  }
  .person__name {
    font-family: "Archivo", sans-serif;
    font-style: italic;
    font-weight: 900;
    font-size: 31px;
    line-height: 1;
    color: var(--orange);
    letter-spacing: 0.5px;
  }
  .person__title {
    font-family: "Archivo", sans-serif;
    font-style: italic;
    font-weight: 900;
    font-size: 19px;
    line-height: 1;
    color: var(--charcoal);
    margin-top: 6px;
    letter-spacing: 0.5px;
  }
  .contacts {
    position: absolute;
    left: 543px;
    top: 224px;
    list-style: none;
  }
  .contacts__item {
    display: flex;
    align-items: center;
    height: 35px;
    font-size: 16.5px;
    font-weight: 500;
    color: var(--charcoal);
  }
  .contacts__icon {
    width: 22px; height: 22px;
    margin-right: 15px;
    flex: none;
  }
  .contacts__at {
    width: 22px;
    margin-right: 15px;
    font-size: 24px;
    font-weight: 600;
    line-height: 1;
    color: var(--orange);
    text-align: center;
  }

  .address-band {
    position: absolute;
    left: 0; right: 0; bottom: 0;
    height: 48px;
    background: var(--orange);
    color: var(--white);
    font-size: 16px;
    font-weight: 600;
    display: flex;
    align-items: center;
    justify-content: center;
  }

  /* Back */
  .back-mark {
    position: absolute;
    left: 320px;
    top: 83px;
    width: 262px; height: 262px;
    border-radius: 50%;
    background: var(--white);
    display: flex;
    align-items: center;
    justify-content: center;
  }
  .back-mark__name {
    font-family: "Figtree", sans-serif;
    font-weight: 700;
    font-size: 24px;
    letter-spacing: 2px;
    color: var(--orange);
    text-align: center;
    line-height: 1.25;
  }
  .social-handle {
    position: absolute;
    left: 0; right: 0;
    top: 410px;
    text-align: center;
    color: var(--white);
    font-size: 19px;
    font-weight: 600;
  }
</style>
</head>
<body>

<section class="card card--front">
  <div class="brand">
    <div class="brand__dot"></div>
    <div class="brand__name">IRON CANYON RIGS</div>
  </div>

  <div class="person">
    <h1 class="person__name">TODD VARNELL</h1>
    <p class="person__title">OWNER</p>
  </div>

  <ul class="contacts">
    <li class="contacts__item">
      <svg class="contacts__icon" viewBox="0 0 24 24" aria-hidden="true">
        <path fill="var(--orange)" d="M6.6 3.5l2.6 3.3c.4.5.3 1.2-.1 1.6L7.6 9.8c1.2 2.6 3.4 4.8 6 6l1.4-1.5c.4-.4 1.1-.5 1.6-.1l3.3 2.6c.5.4.6 1.1.2 1.6l-1.7 2.1c-.5.6-1.300.9-2 .7C9.4 19.6 4.4 14.6 2.8 7.6c-.2-.8.1-1.6.7-2l2.1-1.7c.3-.3.7-.4 1-.4z"/>
        <path fill="none" stroke="var(--orange)" stroke-width="1.6" stroke-linecap="round" d="M14 6.5a4 4 0 0 1 3.5 3.5M14 3a7.5 7.5 0 0 1 7 7"/>
      </svg>
      <span>720-384-9172</span>
    </li>
    <li class="contacts__item">
      <span class="contacts__at" aria-hidden="true">@</span>
      <span>todd@ironcanyonrigs.com</span>
    </li>
    <li class="contacts__item">
      <svg class="contacts__icon" viewBox="0 0 24 24" aria-hidden="true">
        <g fill="none" stroke="var(--orange)" stroke-width="1.4">
          <circle cx="12" cy="12" r="10"/>
          <ellipse cx="12" cy="12" rx="4.5" ry="10"/>
          <path d="M2 12h20M3.5 7h17M3.5 17h17M12 2v20"/>
        </g>
      </svg>
      <span>ironcanyonrogs.com</span>
    </li>
  </ul>

  <div class="address-band">20418 E Pinecrest Service Rd S, STE 310, Cedar Bluff, UT 80517</div>
</section>

<section class="card card--back">
  <div class="back-mark">
    <div class="back-mark__name">IRON<br>CANYON<br>RIGS</div>
  </div>
  <p class="social-handle">@ironcanyonrigs</p>
</section>

</body>
</html>
```